CM Candle Tube Packaging Design

Website: www.corvelmarin.example
IG: @corvel.marin
Tagline: Elevate Your Ambiance
My brand is a sophisticated brand with luxury candles made of coconut wax. Im looking for an upscale minimalist chic design.
Discover the transformative power of positive energy with Corvel Marin candles. Indulge in true luxury with our specially crafted coconut wax blend that not only ignites captivating scents but also embodies modern elegance and empowering elements.
At Corvel Marin we're committed to delivering a unique and exhilarating aromatic experience to all candle lovers. Each candle is meticulously handcrafted in small batches using luxury fragrance oils exclusively formulated for coconut wax.
Our candles are:
Clean-burning
Paraben-Free
Phthalate-Free
Skin-Safe
Pet-Friendly
Look and feel

```html
<!DOCTYPE html>
<html lang="en">
<head>
<meta charset="utf-8">
<title>Corvel Marin — Candle Label</title>
<link rel="stylesheet" href="https://fonts.googleapis.com/css2?family=Italiana&family=Bodoni+Moda:wght@500&family=Allura&family=Poppins:wght@300;400&display=swap">
<style>
  :root {
    --page: #ffffff;
    --label: #dfe2dd;
    --ink: #141925;
    --rule: #b9bdb8;
    --shadow: rgba(40, 45, 50, 0.18);
  }
  html, body {
    margin: 0;
    padding: 0;
    width: 687px;
    height: 1200px;
    overflow: hidden;
    background: var(--page);
  }
  .label {
    position: absolute;
    left: 24px;
    top: 80px;
    width: 640px;
    height: 1040px;
    background: var(--label);
    box-shadow: 0 14px 30px var(--shadow);
    color: var(--ink);
  }
  .row {
    position: absolute;
    left: 0;
    right: 0;
    text-align: center;
    line-height: 1;
  }
  .brand-name {
    top: 330px;
    font-family: "Italiana", serif;
    font-size: 50px;
    letter-spacing: 0.02em;
    display: flex;
    justify-content: center;
    align-items: center;
    gap: 12px;
  }
  .brand-dot {
    width: 8px;
    height: 8px;
    border-radius: 50%;
    background: var(--ink);
  }
  .subline {
    top: 405px;
    font-family: "Poppins", sans-serif;
    font-weight: 300;
    font-size: 15px;
    letter-spacing: 0.36em;
    display: flex;
    justify-content: center;
    align-items: center;
    gap: 14px;
  }
  .subline::before, .subline::after {
    content: "";
    width: 28px;
    height: 1px;
    background: var(--ink);
  }
  .subline::before { margin-right: 2px; }
  .motto {
    top: 432px;
    font-family: "Allura", cursive;
    font-size: 18px;
    opacity: 0.8;
  }
  .headline {
    font-family: "Bodoni Moda", serif;
    font-weight: 500;
    font-size: 76px;
    letter-spacing: -0.01em;
  }
  .headline-elevate { top: 470px; }
  .headline-your { top: 532px; }
  .headline-ambiance {
    top: 588px;
    font-family: "Allura", cursive;
    font-size: 96px;
    font-weight: 400;
  }
  .benefits {
    position: absolute;
    top: 696px;
    left: 175px;
    width: 290px;
    margin: 0;
    padding: 0;
    list-style: none;
    font-family: "Poppins", sans-serif;
    font-size: 13px;
    text-align: center;
  }
  .benefits li {
    height: 33px;
    line-height: 30px;
    border-bottom: 1px solid var(--rule);
  }
  .benefits li:last-child { border-bottom: none; }
  .product-type {
    top: 883px;
    font-family: "Poppins", sans-serif;
    font-size: 16px;
    letter-spacing: 0.3em;
  }
  .product-size {
    top: 912px;
    font-family: "Poppins", sans-serif;
    font-size: 17px;
  }
  .footer-rule {
    position: absolute;
    top: 958px;
    left: 0;
    right: 0;
    display: flex;
    justify-content: center;
    align-items: center;
    gap: 22px;
  }
  .footer-rule .line {
    width: 126px;
    height: 1px;
    background: var(--ink);
  }
  .footer-rule .dot {
    width: 10px;
    height: 10px;
    border-radius: 50%;
    background: var(--ink);
  }
</style>
</head>
<body>
  <main class="label">
    <div class="row brand-name">CORVEL<span class="brand-dot"></span>MARIN</div>
    <div class="row subline">HANDMADE CANDLES</div>
    <div class="row motto">with purpose and love</div>

    <h1 class="row headline headline-elevate" style="margin:0">Elevate</h1>
    <div class="row headline headline-your">Your</div>
    <div class="row headline headline-ambiance">Ambiance</div>

    <ul class="benefits">
      <li>CLEAN-BURNING</li>
      <li>PARABEN-FREE</li>
      <li>PHTHALATE-FREE</li>
      <li>SKIN-SAFE</li>
      <li>PET-FRIENDLY</li>
    </ul>

    <div class="row product-type">COCONUT WAX CANDLE</div>
    <div class="row product-size">14 oz (596 gm)</div>

    <div class="footer-rule">
      <span class="line"></span>
      <span class="dot"></span>
      <span class="line"></span>
    </div>
  </main>
</body>
</html>
```